Guaranteed Job - Sleek Sexy Business Card UV Spot

Im looking for a sleek and sexy business card, that resembles elite or VIP status status.
our business is corinvale.example
you can view our products on there, but our main audience for handing out our cards will be for people in the hospitality industry, so it will need to impress high management and CEO of hotels and restaurants, bars, clubs etc...
the card features will have UV spot on both sides, 400gsm stock. standard size.
Artwork should be 86 x 54mm + 2mm bleed = 90 x 58mm
it should have a nice "unique" uv spot pattern that highlights the card, not a repeated pattern, theres no originality there, and it will be disregarded.
The written material will be:
Corin Vale Hospitality College (logo)
Tobin Marsh
Director
Phone: 1300 615 737
Mobile: 0455 817 296
Email: info@corinvale.example
website: www.corinvale.example
I'm looking for originality here, i don't want just a simple stock card, want something that has a wow factor for people.
You will find the logo attached. you may invert the white to black words to suit the background as you please.
thank you and good luck
As a side note, ive received a lot of proposals, im too busy to give feedback to each and every one, so if i havent provided feedback for your design within 24 hours, then consider it not acceptable, and you could resubmit another design.
So far i have not seen any design that stood out for me, they all seem pretty generic. there nothing thats unique, i would figure for the amount that im offering, that people would put some more effort and creativity into the design.
so far over 200 designs submitted, and nothing i have seen looks very original, everything looks like a different variation of the same stuff, i said it very clearly i wanted something unique, the only thing that has come close to it so far is this one
Reason: Ive received alot of design concepts and i have reviewed everyone, but i havent had time to give feedback to every single one, only the ones that have interested me, if i havent responded, its because i havent found it good enough.
so far only a few design have been on par with what ive been looking for, an attractive eye popping design.
heres a few of them,
http://files.pixelbazaar.example/design_img/51736/62418/62418_2840915_51736_image.jpg
http://files.pixelbazaar.example/design_img/51736/68254/68254_2841377_51736_image.jpg
theyre, both unique and original, and eye catching, the only thing theyre missing is the sexyness.
if you still think you have some creativity left in your minds, then throw it on here.
Reason: Sorry guys for the delay, I was in a serious accident and out of commission for the past few months, I'm just slowly recovering now, please bare with me as i try to attend to this project, it may take me awhile as I have other projects that are on standby, I'm not 100% at the moment, so im extending the deadline for 2 weeks right now. Thanks for your patience.
Hospitality

```html
<!DOCTYPE html>
<html lang="en">
<head>
<meta charset="utf-8">
<title>Corin Vale Hospitality College – Business Card</title>
<link href="https://fonts.googleapis.com/css2?family=Open+Sans:wght@400;600;700&display=swap" rel="stylesheet">
<style>
  :root {
    --page-bg: #e4e5e7;
    --card-blue: #68acdf;
    --band-black: #0b0b0c;
    --ink-white: #ffffff;
    --ink-dark: #111316;
    --ink-soft: #eef5fb;
    --card-w: 660px;
    --card-h: 425px;
    --band-w: 192px;
    --radius: 30px;
  }
  * { box-sizing: border-box; margin: 0; padding: 0; }
  html, body {
    width: 1200px;
    height: 968px;
    overflow: hidden;
    background: var(--page-bg);
    font-family: "Open Sans", Arial, sans-serif;
  }
  .canvas {
    position: relative;
    width: 1200px;
    height: 968px;
    display: flex;
    flex-direction: column;
    align-items: center;
    justify-content: center;
    gap: 36px;
  }
  .card {
    position: relative;
    width: var(--card-w);
    height: var(--card-h);
    border-radius: var(--radius);
    background: var(--card-blue);
    overflow: hidden;
    box-shadow: 0 4px 14px rgba(0, 0, 0, 0.12);
  }
  .card__band {
    position: absolute;
    left: 0;
    top: 0;
    bottom: 0;
    width: var(--band-w);
    background: var(--band-black);
  }
  .brand {
    position: absolute;
    left: 50%;
    bottom: 44px;
    display: flex;
    align-items: center;
    gap: 12px;
    transform: translateX(-50%) rotate(180deg);
    writing-mode: vertical-rl;
    color: var(--ink-white);
    font-weight: 600;
  }
  .brand__mark {
    width: 22px;
    height: 22px;
    background: var(--ink-white);
  }
  .brand__name {
    display: flex;
    flex-direction: row;
    gap: 4px;
    text-transform: uppercase;
    line-height: 1.1;
  }
  .brand__title {
    font-size: 34px;
    letter-spacing: 0.5px;
  }
  .brand__subtitle {
    font-size: 12px;
    letter-spacing: 1.2px;
  }
  .card__web {
    position: absolute;
    right: 54px;
    bottom: 40px;
    font-size: 15px;
    font-weight: 700;
    color: var(--ink-dark);
  }
  .card__person {
    position: absolute;
    left: calc(var(--band-w) + 120px);
    top: 52px;
    display: flex;
    align-items: center;
    gap: 18px;
  }
  .person__role {
    font-size: 15px;
    color: var(--ink-soft);
  }
  .person__divider {
    width: 1px;
    height: 20px;
    background: var(--ink-soft);
  }
  .person__name {
    font-size: 25px;
    font-weight: 700;
    color: var(--ink-dark);
    text-transform: uppercase;
    letter-spacing: 0.3px;
  }
  .card__contact {
    position: absolute;
    left: calc(var(--band-w) + 84px);
    bottom: 44px;
    font-size: 16px;
    line-height: 1.3;
    color: var(--ink-white);
  }
  .contact__group + .contact__group { margin-top: 10px; }
  .contact__label { font-weight: 400; }
</style>
</head>
<body>
<main class="canvas">

  <section class="card card--back" aria-label="Card back">
    <div class="card__band">
      <div class="brand">
        <span class="brand__mark" aria-hidden="true"></span>
        <span class="brand__name">
          <span class="brand__title">Corin Vale</span>
          <span class="brand__subtitle">Hospitality College</span>
        </span>
      </div>
    </div>
    <p class="card__web">www.corinvale.example</p>
  </section>

  <section class="card card--front" aria-label="Card front">
    <div class="card__band">
      <div class="brand">
        <span class="brand__mark" aria-hidden="true"></span>
        <span class="brand__name">
          <span class="brand__title">Corin Vale</span>
          <span class="brand__subtitle">Hospitality College</span>
        </span>
      </div>
    </div>

    <div class="card__person">
      <span class="person__role">Director</span>
      <span class="person__divider" aria-hidden="true"></span>
      <span class="person__name">Tobin Marsh</span>
    </div>

    <div class="card__contact">
      <div class="contact__group">
        <p><span class="contact__label">Phone:</span> 1300 615 737</p>
        <p><span class="contact__label">Mobile:</span> 0455 817 296</p>
      </div>
      <div class="contact__group">
        <p><span class="contact__label">Email:</span> info@corinvale.example</p>
        <p><span class="contact__label">Web:</span> www.corinvale.example</p>
      </div>
    </div>
  </section>

</main>
</body>
</html>
```